Business Cards for Branding (Advertising) Agency

We need stylish and cool business cards.
Additional info:
1) Logo - see the attachment. You can use either the three penguins or just one penguin face (square or round) - at your discretion.
2) Text and other stuff for business card:
front side:
-Logo and company name: company name - Coastal Herons - should be in English as is in logo. This is the only exception. The rest of the text will be in Russian.
-Who we are: Брендинговое агентство
-First and last name:
-Position: Управляющий партнёр
-Address:
-Phone:
-Email:
-Website:
Note: please don't use names of information fields, such as: who we are, first and last name, position, address, phone, email and website.

3) Our suggestions on design:
-The backside of the business card can be either blank or has something on it - at your discretion.
-The business card background should be either white or grey (you can use any tone of grey).

Additional Information:
1) БРЕНДИНГОВОЕ АГЕНТСТВО
2) ул. Вересковая - these two words should be together on the same line
3) тел.: +7 (495) 381-62-09
моб.: +7 (916) 740-28-51

Reason: We would like to receive more stylish designs.

```html
<!DOCTYPE html>
<html lang="ru">
<head>
<meta charset="utf-8">
<title>Coastal Herons — визитка</title>
<link rel="stylesheet" href="https://fonts.googleapis.com/css2?family=Open+Sans:wght@400;600&family=Tinos&display=swap">
<style>
  :root {
    --backdrop: #2b2b2b;
    --card: #ffffff;
    --card-back: #c6c6c6;
    --ink: #1a1a1a;
    --ink-soft: #6d6d6d;
    --rule: #cfcfcf;
    --rule-dark: #b3b3b3;
    --mark: #2a2a2a;
  }
  * { margin: 0; padding: 0; box-sizing: border-box; }
  html, body { width: 1200px; height: 900px; overflow: hidden; }
  body { background: var(--backdrop); font-family: "Open Sans", Arial, sans-serif; position: relative; }

  .card { position: absolute; left: 250px; width: 700px; height: 400px; overflow: hidden; }

  /* back side */
  .card--back { top: 33px; background: var(--card-back); }
  .lockup {
    position: absolute; left: 0; right: 0; top: 150px;
    display: flex; align-items: center; justify-content: center; gap: 22px;
  }
  .lockup__dot { width: 78px; height: 78px; border-radius: 50%; background: var(--mark); flex: none; }
  .lockup__text { display: flex; flex-direction: column; }
  .lockup__name { font-size: 44px; font-weight: 400; color: var(--mark); letter-spacing: 2px; line-height: 1.1; }
  .lockup__site { font-size: 16px; color: var(--mark); align-self: flex-end; }

  /* front side */
  .card--front { top: 467px; background: var(--card); color: var(--ink); }
  .card__band {
    position: absolute; left: 0; right: 0; bottom: 18px; height: 7px;
    background: var(--rule);
  }
  .card__band::after {
    content: ""; position: absolute; left: 0; right: 0; bottom: -3px; height: 1px;
    background: var(--rule-dark);
  }
  .brand {
    position: absolute; left: 36px; top: 168px; width: 320px;
    display: flex; align-items: center; gap: 14px;
  }
  .brand__dot { width: 44px; height: 44px; border-radius: 50%; background: var(--mark); flex: none; }
  .brand__name { font-size: 30px; font-weight: 600; color: var(--mark); letter-spacing: 0.5px; white-space: nowrap; }
  .info { position: absolute; left: 400px; top: 46px; width: 290px; }
  .info__tagline { font-size: 24px; line-height: 1.1; font-weight: 400; }
  .info__name { margin-top: 28px; font-size: 21px; color: var(--ink-soft); line-height: 1.1; }
  .info__role { font-size: 15px; }
  .contacts { list-style: none; margin-top: 36px; font-family: "Tinos", "Times New Roman", serif; font-size: 14.5px; }
  .contacts li { display: flex; align-items: flex-start; gap: 9px; margin-bottom: 6px; line-height: 1.2; }
  .contacts svg { width: 13px; height: 13px; flex: none; margin-top: 2px; fill: var(--ink-soft); }
</style>
</head>
<body>
  <article class="card card--back">
    <div class="lockup">
      <span class="lockup__dot"></span>
      <span class="lockup__text">
        <span class="lockup__name">Coastal Herons</span>
        <span class="lockup__site">coastalherons.ru</span>
      </span>
    </div>
  </article>

  <article class="card card--front">
    <div class="brand">
      <span class="brand__dot"></span>
      <span class="brand__name">Coastal Herons</span>
    </div>

    <section class="info">
      <h1 class="info__tagline">Брендинговое<br>агентство</h1>
      <p class="info__name">Марина Ольховская</p>
      <p class="info__role">Управляющий партнёр</p>
      <ul class="contacts">
        <li><svg viewBox="0 0 24 24"><path d="M6.6 10.8a15 15 0 0 0 6.6 6.6l2.2-2.2c.3-.3.7-.4 1-.2 1.1.4 2.3.6 3.6.6.6 0 1 .4 1 1V20c0 .6-.4 1-1 1C10.6 21 3 13.4 3 4c0-.6.4-1 1-1h3.5c.6 0 1 .4 1 1 0 1.3.2 2.5.6 3.6.1.3 0 .7-.2 1z"/></svg>+7 (916) 740-28-51</li>
        <li><svg viewBox="0 0 24 24"><path d="M3 5h18v14H3zm2 2v.5l7 4.5 7-4.5V7zm0 2.8V17h14V9.8l-7 4.5z"/></svg>marina@coastalherons.ru</li>
        <li><svg viewBox="0 0 24 24"><path d="M12 2a10 10 0 1 0 0 20 10 10 0 0 0 0-20zm-1 17.9A8 8 0 0 1 4.1 11L9 16v1a2 2 0 0 0 2 2zm6.9-2.5A2 2 0 0 0 16 16h-1v-3a1 1 0 0 0-1-1H8v-2h2a1 1 0 0 0 1-1V7h2a2 2 0 0 0 2-2v-.4a8 8 0 0 1 2.9 12.8z"/></svg>www.coastalherons.ru</li>
        <li><svg viewBox="0 0 24 24"><path d="M12 2a7 7 0 0 0-7 7c0 5.2 7 13 7 13s7-7.8 7-13a7 7 0 0 0-7-7zm0 9.5A2.5 2.5 0 1 1 12 6.5a2.5 2.5 0 0 1 0 5z"/></svg><span>117208, г. Москва, ул. Вересковая,<br>д.12, стр.5</span></li>
      </ul>
    </section>

    <div class="card__band"></div>
  </article>
</body>
</html>
```